Postcard Design

We are a small day care chain operating out of two adjacent homes. We need a design that illustrates a caring loving environment and focuses on the services we provide, our low weekly rates, and urge the receiver of the postcard to enroll now. Our services are: open 24 hours, Saturday care available, Camera surveillance system, small provider to student ratio, kindergarten preparedness program, tutoring, introduction to Spanish, music, art, gym, after school program, NQBT membership, transportation from and to home, school drop off and pick up, 3 meals and 3 snacks served daily. Our rates: starting as low as $78.22 a week and we accept KVD, employer, and military assistance. Certifications: State of Ohio licensed, Brindle County trained and certified, ZRPA trained. We are offering a wavier on the registration fee and space is limited. We would like are postcards to have the color shades of blue, green and yellow. Contact info: 555 271 9043 call for tour and visit us @ HartwellFamilyDayCare.example and on Facebook @ Hartwell Family Day Care. Location: across from the Delcourt Playhouse. Serving ages 6 weeks to 12 years. These details must be noticeably displayed. Also our name Hartwell Family Day Care must be displayed on both sides.
Updates

We would like for the postcard to highlight our torturing pprogram and to say "ask about NQBT Membership"

Target Market(s)

young (ages 18-35)women with children

Industry/Entity Type

Environment

Requirements
Must have
• personality and character must stand out

```html
<!DOCTYPE html>
<html lang="en">
<head>
<meta charset="utf-8">
<title>Hartwell Family Day Care – Postcard</title>
<link rel="stylesheet" href="https://fonts.googleapis.com/css2?family=Oswald:wght@400;500;600&family=Arimo:wght@400;700&display=swap">
<style>
  :root {
    --page-bg: #ececec;
    --teal-dark: #0a4c66;
    --teal: #0f6f8d;
    --teal-light: #1a93b3;
    --title-green: #79bf3f;
    --wave-green: #7cc242;
    --sun-yellow: #ffe600;
    --ribbon-yellow: #f7d41c;
    --ink-blue: #14557a;
    --contact-blue: #2f7ea4;
    --white: #ffffff;
    --photo-light: #eef0ef;
    --photo-warm: #e4d8cc;
  }
  * { box-sizing: border-box; margin: 0; padding: 0; }
  html, body { width: 1200px; height: 848px; overflow: hidden; }
  body { background: var(--page-bg); position: relative; font-family: "Arimo", Arial, sans-serif; }

  .postcard { position: absolute; overflow: hidden; background: var(--white); }
  .postcard--front { left: 55px; top: 195px; width: 540px; height: 417px; }
  .postcard--back { left: 619px; top: 253px; width: 538px; height: 417px; }

  .photo { position: absolute; left: 0; top: 0; }
  .front-photo { width: 540px; height: 270px;
    background: linear-gradient(100deg, var(--photo-warm) 0%, #f3ece6 30%, var(--photo-light) 60%, #f7f7f7 100%); }
  .wave-art { position: absolute; left: 0; top: 0; }

  .front-title { position: absolute; right: 22px; top: 26px; white-space: nowrap; text-align: right;
    font-family: "Oswald", sans-serif; font-weight: 600; font-size: 28px; line-height: 36px;
    color: var(--title-green); letter-spacing: -0.3px; }

  .rate-badge { position: absolute; left: 401px; top: 139px; width: 112px; height: 112px; border-radius: 50%;
    background: var(--wave-green); display: flex; align-items: center; justify-content: center; }
  .rate-badge::before { content: ""; position: absolute; inset: 5px; border: 2px dashed var(--white); border-radius: 50%; }
  .rate-badge p { width: 84px; text-align: center; color: var(--white); font-family: "Oswald", sans-serif;
    font-weight: 500; font-size: 11px; line-height: 11.5px; }

  .ribbon { position: absolute; height: 24px; }
  .ribbon__tab { position: absolute; left: 0; top: 0; height: 24px; background: var(--ribbon-yellow); }
  .ribbon__label { position: absolute; top: 0; height: 24px; padding: 0 16px 0 6px; background: var(--sun-yellow);
    font-family: "Oswald", sans-serif; font-weight: 600; font-size: 19px; line-height: 24px; color: var(--ink-blue);
    clip-path: polygon(0 0, 100% 0, 92% 50%, 100% 100%, 0 100%); white-space: nowrap; }

  .cert-ribbon { left: 0; top: 258px; width: 200px; }
  .cert-ribbon .ribbon__tab { width: 50px; }
  .cert-ribbon .ribbon__label { left: 45px; }
  .cert-text { position: absolute; left: 62px; top: 284px; color: var(--white); font-size: 13px; white-space: nowrap; }

  .offer-band { position: absolute; left: 80px; top: 320px; width: 460px; height: 23px;
    background: linear-gradient(90deg, rgba(255,255,255,0) 0%, rgba(150,210,230,0.55) 35%, rgba(160,215,235,0.6) 100%); }
  .offer-band p { position: absolute; right: 18px; top: 0; line-height: 23px; color: var(--white);
    font-family: "Oswald", sans-serif; font-weight: 500; font-size: 15.5px; white-space: nowrap; }

  .contact-strip { position: absolute; left: 0; top: 353px; width: 540px; height: 37px; background: var(--white);
    display: flex; align-items: center; justify-content: space-between; padding: 0 18px; }
  .contact-item { display: flex; align-items: center; gap: 5px; font-family: "Oswald", sans-serif; font-weight: 500;
    font-size: 14px; color: var(--contact-blue); white-space: nowrap; }
  .contact-dot { width: 22px; height: 22px; border-radius: 50%; background: var(--teal); flex: none;
    display: flex; align-items: center; justify-content: center; }
  .foot-band { position: absolute; left: 0; top: 390px; width: 100%; height: 27px;
    background: linear-gradient(90deg, var(--teal-dark), var(--teal-light) 50%, var(--teal-dark)); }

  /* Back side */
  .back-panel { position: absolute; left: 0; top: 0; width: 261px; height: 417px; overflow: hidden; }
  .back-photo { width: 261px; height: 175px; background: linear-gradient(110deg, #6aa45a 0%, #d6b24a 40%, #e8c870 70%, #c88a5a 100%); }
  .back-title { position: absolute; left: 0; width: 261px; top: 17px; text-align: center; font-family: "Oswald", sans-serif;
    font-weight: 600; font-size: 23px; color: var(--white); letter-spacing: -0.2px; white-space: nowrap; }
  .services-ribbon { left: 0; top: 170px; width: 200px; }
  .services-ribbon .ribbon__tab { width: 50px; }
  .services-ribbon .ribbon__label { left: 45px; }
  .service-list { position: absolute; left: 47px; top: 200px; width: 200px; list-style: none; color: var(--white);
    font-size: 10.6px; line-height: 11.4px; }
  .service-list li { position: relative; padding-left: 12px; }
  .service-list li::before { content: ""; position: absolute; left: 1px; top: 3px; width: 6px; height: 6px;
    border-radius: 50%; background: var(--white); }
  .back-contact { position: absolute; left: 0; top: 359px; width: 261px; height: 36px; background: var(--white);
    display: flex; align-items: center; justify-content: flex-end; gap: 5px; padding-right: 11px; }
  .back-contact__label { font-family: "Oswald", sans-serif; font-weight: 500; font-size: 9px; line-height: 9px;
    text-align: right; color: var(--ink-blue); }
  .back-contact__dot { width: 30px; height: 30px; }
  .back-contact__number { font-family: "Oswald", sans-serif; font-weight: 600; font-size: 22px; color: var(--contact-blue); white-space: nowrap; }
  .back-foot { position: absolute; left: 0; top: 395px; width: 261px; height: 22px;
    background: linear-gradient(90deg, var(--teal-dark), var(--teal-light) 60%, var(--teal-dark)); }
  .address-area { position: absolute; left: 261px; top: 0; width: 277px; height: 417px; background: var(--white); }
</style>
</head>
<body>

  <section class="postcard postcard--front">
    <div class="photo front-photo" role="img" aria-label="Photo of a caregiver exploring a globe with a young girl in a bright classroom"></div>
    <svg class="wave-art" width="540" height="417" viewBox="0 0 540 417" aria-hidden="true">
      <defs>
        <linearGradient id="frontTeal" x1="0" y1="0" x2="1" y2="1">
          <stop offset="0" stop-color="#0c6a87"/>
          <stop offset="0.55" stop-color="#0f7f9f"/>
          <stop offset="1" stop-color="#0a4c66"/>
        </linearGradient>
      </defs>
      <path d="M190,250 C320,250 440,205 540,135 L540,185 C450,235 340,262 230,262 Z" fill="var(--wave-green)"/>
      <path d="M0,245 C120,262 260,268 370,240 C450,220 500,195 540,180 L540,417 L0,417 Z" fill="url(#frontTeal)"/>
      <path d="M0,245 C120,262 260,268 370,240 C450,220 500,195 540,180" fill="none" stroke="var(--sun-yellow)" stroke-width="6"/>
    </svg>

    <h1 class="front-title">Hartwell Family Day Care</h1>

    <div class="rate-badge">
      <p>Starting as low as $78.22 a week and we accept KVD, employer, and military assistance</p>
    </div>

    <div class="ribbon cert-ribbon">
      <span class="ribbon__tab"></span>
      <h2 class="ribbon__label">Certifications</h2>
    </div>
    <p class="cert-text">State of Ohio licensed, Brindle County trained and certified, ZRPA trained.</p>

    <div class="offer-band">
      <p>We are offering a wavier on the registration fee and space is limited</p>
    </div>

    <div class="contact-strip">
      <span class="contact-item"><span class="contact-dot"></span>Hartwell Family Day Care</span>
      <span class="contact-item">
        <span class="contact-dot">
          <svg width="15" height="15" viewBox="0 0 16 16" aria-hidden="true"><circle cx="8" cy="8" r="6.5" fill="none" stroke="#fff" stroke-width="1.3"/><ellipse cx="8" cy="8" rx="3" ry="6.5" fill="none" stroke="#fff" stroke-width="1.1"/><path d="M1.5 8h13M2.5 4.8h11M2.5 11.2h11" stroke="#fff" stroke-width="1"/></svg>
        </span>HartwellFamilyDayCare.example</span>
      <span class="contact-item">
        <span class="contact-dot">
          <svg width="13" height="13" viewBox="0 0 16 16" aria-hidden="true"><path d="M4 1.5l2.5 3-1.6 1.8c.8 1.8 2.4 3.4 4.3 4.3l1.8-1.6 3 2.5-1.8 2.3C7.3 13.6 2.4 8.7 1.7 3.3Z" fill="#fff"/></svg>
        </span>555 271 9043</span>
    </div>
    <div class="foot-band"></div>
  </section>

  <section class="postcard postcard--back">
    <div class="back-panel">
      <div class="photo back-photo" role="img" aria-label="Photo of toddlers playing with toys at a classroom table"></div>
      <svg class="wave-art" width="261" height="417" viewBox="0 0 261 417" aria-hidden="true">
        <defs>
          <linearGradient id="backTeal" x1="0" y1="0" x2="0.6" y2="1">
            <stop offset="0" stop-color="#0f7f9f"/>
            <stop offset="1" stop-color="#0a4c66"/>
          </linearGradient>
        </defs>
        <path d="M0,138 C60,160 130,175 190,170 C220,167 245,160 261,150 L261,417 L0,417 Z" fill="url(#backTeal)"/>
        <path d="M0,138 C60,160 130,175 190,170 C220,167 245,160 261,150" fill="none" stroke="var(--sun-yellow)" stroke-width="5"/>
      </svg>
      <h1 class="back-title">Hartwell Family Day Care</h1>

      <div class="ribbon services-ribbon">
        <span class="ribbon__tab"></span>
        <h2 class="ribbon__label">Our services</h2>
      </div>
      <ul class="service-list">
        <li>Open 24 hours</li>
        <li>Saturday care available,</li>
        <li>Camera surveillance system,</li>
        <li>Small provider to student ratio,</li>
        <li>kindergarten preparedness program,</li>
        <li>Tutoring, introduction to Spanish,</li>
        <li>Music, art, gym,</li>
        <li>After school program,</li>
        <li>NQBT membership,</li>
        <li>Transportation from and to home,<br>school drop off and pick up,</li>
        <li>3 meals and 3 snacks served daily</li>
      </ul>

      <div class="back-contact">
        <span class="back-contact__label">CONTACT<br>INFO</span>
        <span class="contact-dot back-contact__dot">
          <svg width="17" height="17" viewBox="0 0 16 16" aria-hidden="true"><path d="M4 1.5l2.5 3-1.6 1.8c.8 1.8 2.4 3.4 4.3 4.3l1.8-1.6 3 2.5-1.8 2.3C7.3 13.6 2.4 8.7 1.7 3.3Z" fill="#fff"/></svg>
        </span>
        <span class="back-contact__number">555 271 9043</span>
      </div>
      <div class="back-foot"></div>
    </div>
    <div class="address-area"></div>
  </section>

</body>
</html>
```